Kitchen and bathroom exhaust fan cleaning business card design

A new business cleaning domestic - not commercial - exhaust/extractor fans in kitchens, bathrooms and en suites and kitchen range hood filters.

We would like a bright colour suggesting cleanliness (such a syellow or light green?)

I would like to see on the card preferably on the reverse:

"We clean kitchen and bathroom exhaust fans & Volrex Brightos
and
clean and repair range hood filters and replace carbon filters

We give Pensioner discounts
Updates

Designers pls note the TM in the contact filed after Pureflow Vents should be superscript as in the trademark sign. On the reverse of the card, I would like:: "We clean kitchen and bathroom exhaust fans & Volrex Brightos & clean and repair range hood filters and replace carbon filters We give Pensioner discounts

Reason: I will be out of the country for several days

Target Market(s)

people who are too lazy or too busy to clean their fan units and pensioners and others who are unable to do it.

Industry/Entity Type

Business

Contact Information for Business Card

ACT Clean FansTM Designer pls note the TM should be superscript as in the trademark sign
Neil Oakley
Mob: 0431 572 864
Email: pureflowvents@zentromail.com
PO Box 7152, Pellow ACT 2608

Requirements
Must have
• Designer pls note the TM in the contact filed after Pureflow Vents should be superscript as in the trademark sign.

On the reverse

and

```html
<!DOCTYPE html>
<html lang="en">
<head>
<meta charset="utf-8">
<title>Pureflow Vents – Business Card</title>
<link rel="stylesheet" href="https://fonts.googleapis.com/css2?family=Tenor+Sans&family=PT+Sans:wght@400;700&display=swap">
<style>
  :root {
    --page-bg: #e4e4e4;
    --card-yellow: #ffff1a;
    --card-yellow-edge: #d9d900;
    --accent-green: #19d619;
    --accent-green-dark: #12b812;
    --ink: #111111;
    --band-text: #c8ffb0;
    --fixture-light: #f2f2f2;
    --fixture-mid: #c9c9c9;
  }
  * { box-sizing: border-box; margin: 0; padding: 0; }
  html, body {
    width: 1200px; height: 1200px; overflow: hidden;
    background: var(--page-bg);
  }
  .canvas {
    position: relative; width: 1200px; height: 1200px;
    display: flex; flex-direction: column; align-items: center; justify-content: center; gap: 56px;
  }
  .card {
    position: relative; width: 900px; height: 514px; overflow: hidden;
    background: radial-gradient(ellipse at 55% 45%, #ffff6a 0%, var(--card-yellow) 45%, var(--card-yellow-edge) 100%);
    box-shadow: 0 6px 18px rgba(0,0,0,.18);
    font-family: "PT Sans", sans-serif; color: var(--ink);
  }
  .brand {
    position: absolute; font-family: "Tenor Sans", sans-serif; font-size: 40px;
    letter-spacing: .5px; white-space: nowrap; line-height: 1;
  }
  .tm {
    display: inline-block; vertical-align: top; font-family: "PT Sans", sans-serif;
    font-size: 11px; font-weight: 700; width: 26px; height: 26px; line-height: 23px;
    text-align: center; border: 2px solid var(--ink); border-radius: 50%;
    margin-left: 4px; position: relative; top: -18px;
  }
  /* front */
  .front .band-top {
    position: absolute; left: 560px; top: 60px; width: 340px; height: 66px; background: var(--accent-green);
  }
  .front .band-left {
    position: absolute; left: 0; top: 226px; width: 124px; height: 64px; background: var(--accent-green);
  }
  .front .brand { left: 136px; top: 240px; }
  .front .person-name { position: absolute; left: 640px; top: 146px; font-size: 38px; line-height: 1.2; white-space: nowrap; }
  .front .contact-list {
    position: absolute; left: 460px; top: 300px; list-style: none; font-size: 25px; line-height: 46px; white-space: nowrap;
  }
  .front .fixture {
    position: absolute; background: linear-gradient(160deg, var(--fixture-light), var(--fixture-mid));
  }
  .front .fixture-round { left: 40px; top: 330px; width: 170px; height: 140px; border-radius: 50%; }
  .front .fixture-square { left: 230px; top: 380px; width: 140px; height: 110px; border-radius: 12px; }
  /* back */
  .back .brand { left: 70px; top: 50px; }
  .back .service-list {
    position: absolute; left: 78px; top: 128px; list-style: none; font-size: 25px; line-height: 38px;
  }
  .back .service-list li { position: relative; padding-left: 34px; }
  .back .service-list li svg { position: absolute; left: 0; top: 11px; }
  .back .promise-band { position: absolute; left: 0; bottom: 0; width: 900px; height: 120px; }
  .back .promise-text {
    position: absolute; left: 80px; bottom: 34px; font-size: 26px; color: var(--band-text);
  }
</style>
</head>
<body>
<main class="canvas">

  <section class="card front" aria-label="Card front">
    <div class="band-top"></div>
    <div class="band-left"></div>
    <div class="brand">PUREFLOW VENTS<span class="tm">TM</span></div>
    <div class="person-name">Neil Oakley</div>
    <ul class="contact-list">
      <li>Mob: 0431 572 864</li>
      <li>PO Box 7152, Pellow ACT 2608</li>
      <li>Email: pureflowvents@zentromail.com</li>
    </ul>
    <div class="fixture fixture-round" role="img" aria-label="Photo of a round ceiling exhaust fan"></div>
    <div class="fixture fixture-square" role="img" aria-label="Photo of a bathroom heat lamp and fan unit"></div>
  </section>

  <section class="card back" aria-label="Card back">
    <div class="brand">PUREFLOW VENTS<span class="tm">TM</span></div>
    <ul class="service-list">
      <li><svg width="14" height="16" viewBox="0 0 14 16"><path d="M0 0 L14 8 L0 16 L4 8 Z" fill="#111"/></svg>Clean Kitchen, Bathroom &amp; en suite Exhaust Fans</li>
      <li><svg width="14" height="16" viewBox="0 0 14 16"><path d="M0 0 L14 8 L0 16 L4 8 Z" fill="#111"/></svg>Clean range hood filters offsite</li>
      <li><svg width="14" height="16" viewBox="0 0 14 16"><path d="M0 0 L14 8 L0 16 L4 8 Z" fill="#111"/></svg>Replace old charcoal filters</li>
      <li><svg width="14" height="16" viewBox="0 0 14 16"><path d="M0 0 L14 8 L0 16 L4 8 Z" fill="#111"/></svg>Repair range hood filters.</li>
      <li><svg width="14" height="16" viewBox="0 0 14 16"><path d="M0 0 L14 8 L0 16 L4 8 Z" fill="#111"/></svg>Clean anything else you want.</li>
    </ul>
    <svg class="promise-band" viewBox="0 0 900 120" preserveAspectRatio="none" aria-hidden="true">
      <polygon points="60,20 900,20 900,120 0,120" fill="var(--accent-green-dark)"/>
    </svg>
    <div class="promise-text">We are fully Insured and give Pensioner Discounts</div>
  </section>

</main>
</body>
</html>
```